Consulting Company needs business card design

We need a business card design for a new consulting and business solutions company based in Bermuda called Corvale Partners Limited. Looking for a double sided business card with one side only including the company logo thats attached and the other including contact information. Logo contains blue and turquoise colors and is fine to be on both sides of the card.
Contact Information for Business Card
Corvale Partners Limited
P.O. Box HM318
Devonshire DV BX
Bermuda
Name: Marcus Pellegrin
Position: Director
Telephone: 1 441 733 4906
Email: mpellegrin@corvale.example
Website: www.corvale.example

```html
<!DOCTYPE html>
<html lang="en">
<head>
<meta charset="utf-8">
<title>Corvale Partners Limited – Business Card</title>
<link rel="stylesheet" href="https://fonts.googleapis.com/css2?family=Lato:wght@400;700&family=Open+Sans:wght@400;600;700&display=swap">
<style>
  :root {
    --backdrop: #8c8c8c;
    --card-front: #f3f3f3;
    --brand-blue: #29a8e0;
    --brand-teal: #00b3bb;
    --ink: #1f1f1f;
    --rule: #9a9a9a;
    --white: #ffffff;
  }
  * { margin: 0; padding: 0; box-sizing: border-box; }
  html, body { width: 1200px; height: 1200px; overflow: hidden; }
  body { background: var(--backdrop); position: relative; font-family: "Lato", sans-serif; }

  .card {
    position: absolute;
    top: 310px;
    width: 363px;
    height: 594px;
    border-radius: 18px;
    overflow: hidden;
  }
  .card--front { left: 234px; background: var(--card-front); text-align: center; color: var(--ink); }
  .card--back { left: 630px; width: 366px; background: var(--brand-teal); }

  .brand {
    position: absolute;
    top: 140px; left: 0; right: 0;
    display: flex; align-items: center; justify-content: center; gap: 12px;
  }
  .brand__dot { width: 44px; height: 44px; border-radius: 50%; background: var(--brand-teal); }
  .brand__name {
    font-family: "Open Sans", sans-serif;
    font-weight: 600;
    font-size: 25px;
    line-height: 1.1;
    letter-spacing: 1px;
    color: var(--brand-blue);
    text-align: left;
  }

  .person { position: absolute; top: 306px; left: 0; right: 0; }
  .person__name {
    font-family: "Open Sans", sans-serif;
    font-weight: 600; font-size: 22px; color: var(--brand-blue);
    letter-spacing: 0.3px;
  }
  .person__role { font-size: 17px; margin-top: 2px; }

  .contact-rule {
    position: absolute; top: 369px; left: 91px; width: 187px; height: 20px;
  }
  .contact-list { position: absolute; top: 395px; left: 0; right: 0; font-size: 17px; line-height: 22px; }
  .divider { position: absolute; top: 471px; left: 91px; width: 187px; height: 1px; background: var(--rule); }
  .company { position: absolute; top: 484px; left: 0; right: 0; font-size: 17px; line-height: 21.5px; }
  .company__name { color: var(--brand-blue); letter-spacing: 0.2px; }

  .back-band { position: absolute; inset: 0; }
  .back-name {
    position: absolute; top: 262px; left: 0; right: 0; text-align: center;
    font-family: "Open Sans", sans-serif; font-weight: 700; font-size: 34px;
    color: var(--white); letter-spacing: 3px;
  }
  .back-url {
    position: absolute; top: 524px; left: 0; right: 0; text-align: center;
    font-family: "Open Sans", sans-serif; font-weight: 600; font-size: 17px;
    color: var(--white); letter-spacing: 2px;
  }
</style>
</head>
<body>

<section class="card card--front" aria-label="Contact side">
  <div class="brand">
    <span class="brand__dot"></span>
    <span class="brand__name">CORVALE<br>PARTNERS</span>
  </div>

  <div class="person">
    <h1 class="person__name">MARCUS PELLEGRIN</h1>
    <p class="person__role">Director</p>
  </div>

  <svg class="contact-rule" viewBox="0 0 187 20" aria-hidden="true">
    <line x1="0" y1="10" x2="56" y2="10" stroke="#9a9a9a" stroke-width="1"/>
    <line x1="131" y1="10" x2="187" y2="10" stroke="#9a9a9a" stroke-width="1"/>
    <circle cx="68" cy="10" r="9.5" fill="#29a8e0"/>
    <path d="M64 5.5c1-.6 1.8.8 2 1.8.1.6-.8 1-.6 1.6.5 1.3 1.5 2.3 2.8 2.8.6.2 1-.7 1.6-.6 1 .2 2.4 1 1.8 2-.6 1-1.9 1.3-3 .9-2.6-1-4.6-3-5.6-5.6-.4-1.1-.1-2.4 1-2.9z" fill="#fff"/>
    <circle cx="91" cy="10" r="9.5" fill="#29a8e0"/>
    <rect x="85.5" y="6" width="11" height="8" rx="1" fill="#fff"/>
    <path d="M85.8 6.5l5.2 4 5.2-4" fill="none" stroke="#29a8e0" stroke-width="1"/>
    <circle cx="114" cy="10" r="9.5" fill="#29a8e0"/>
    <circle cx="114" cy="10" r="5.5" fill="none" stroke="#fff" stroke-width="1.3"/>
    <path d="M108.5 10h11M114 4.5c-2.5 3-2.5 8 0 11M114 4.5c2.5 3 2.5 8 0 11" fill="none" stroke="#fff" stroke-width="1"/>
  </svg>

  <div class="contact-list">
    <p>1 441 733 4906</p>
    <p>mpellegrin@corvale.example</p>
    <p>www.corvale.example</p>
  </div>

  <div class="divider"></div>

  <div class="company">
    <p class="company__name">CORVALE PARTNERS LIMITED</p>
    <p>P.O. Box HM318</p>
    <p>Devonshire DV BX Bermuda</p>
  </div>
</section>

<section class="card card--back" aria-label="Brand side">
  <svg class="back-band" viewBox="0 0 366 594" preserveAspectRatio="none" aria-hidden="true">
    <path d="M0 0H366V110C250 130 120 140 0 300Z" fill="#29a8e0"/>
  </svg>
  <p class="back-name">CORVALE</p>
  <p class="back-url">WWW.CORVALE.EXAMPLE</p>
</section>

</body>
</html>
```